Training Manual

We need a black/white InDesign template created for our training manual. We're looking to slightly modernize the design and make it as visually appealing as possible while also remaining highly-readable and not tiring to look at at for long periods of time.
A sample chapter from our current manual is attached. - The manual overall consists of 260 pages, there are a few diagrams but the manual consists primarily of text.
Training

```html
<!DOCTYPE html>
<html lang="en">
<head>
<meta charset="utf-8">
<title>05 The Devotional Life</title>
<link rel="stylesheet" href="https://fonts.googleapis.com/css2?family=Inter:ital,wght@0,300;0,400;0,700;0,800;1,400&display=swap">
<style>
  :root {
    --paper: #ffffff;
    --ink: #1a1a1a;
    --rule: #cfcfcf;
    --mark: #9a9a9a;
    --placeholder: #d3d1d1;
  }
  * { margin: 0; padding: 0; box-sizing: border-box; }
  html, body { width: 1200px; height: 1000px; overflow: hidden; background: var(--paper); }
  body { position: relative; font-family: "Inter", Helvetica, Arial, sans-serif; color: var(--ink); }

  .trim { position: absolute; inset: 0; }

  .running-head {
    position: absolute; left: 55px; top: 124px;
    font-size: 7px; font-style: italic; letter-spacing: -0.1px;
  }
  .chapter-title {
    position: absolute; left: 53px; top: 280px;
    font-size: 35px; line-height: 1; letter-spacing: -0.6px; font-weight: 800; white-space: nowrap;
  }
  .chapter-title .chapter-number { font-weight: 300; margin-right: 8px; }

  .column {
    position: absolute; width: 514px;
    font-size: 7.9px; line-height: 10px; letter-spacing: 0.02px;
  }
  .column-left { left: 55px; top: 378px; }
  .column-right { left: 633px; top: 497px; }

  .section-heading { font-size: 9.5px; font-weight: 700; line-height: 12px; margin-bottom: 9px; letter-spacing: 0; }
  .section-heading .subtitle { font-weight: 400; }
  .column p { margin-bottom: 10px; }
  .column p.quote { font-style: italic; }
  .marker { font-weight: 700; }

  .feature-image {
    position: absolute; left: 633px; top: 131px; width: 514px; height: 347px;
    background: var(--placeholder);
  }

  .folio {
    position: absolute; right: 55px; top: 868px;
    font-size: 7px; font-style: italic;
  }
  .folio .page-number { font-style: normal; font-weight: 700; margin-left: 14px; }
</style>
</head>
<body>

<svg class="trim" width="1200" height="1000" viewBox="0 0 1200 1000" aria-hidden="true">
  <g stroke="var(--rule)" stroke-width="1" fill="none">
    <line x1="20.5" y1="88" x2="20.5" y2="908"/>
    <line x1="600.5" y1="88" x2="600.5" y2="908"/>
    <line x1="1179.5" y1="88" x2="1179.5" y2="908"/>
    <line x1="20" y1="88.5" x2="1180" y2="88.5"/>
    <line x1="20" y1="907.5" x2="1180" y2="907.5"/>
  </g>
  <g stroke="var(--mark)" stroke-width="1">
    <line x1="20.5" y1="66" x2="20.5" y2="80"/>
    <line x1="600.5" y1="66" x2="600.5" y2="80"/>
    <line x1="1179.5" y1="66" x2="1179.5" y2="80"/>
    <line x1="0" y1="88.5" x2="12" y2="88.5"/>
    <line x1="1188" y1="88.5" x2="1200" y2="88.5"/>
    <line x1="20.5" y1="916" x2="20.5" y2="930"/>
    <line x1="600.5" y1="916" x2="600.5" y2="930"/>
    <line x1="1179.5" y1="916" x2="1179.5" y2="930"/>
    <line x1="0" y1="907.5" x2="12" y2="907.5"/>
    <line x1="1188" y1="907.5" x2="1200" y2="907.5"/>
  </g>
</svg>

<div class="running-head">05 The Devotional Life</div>

<h1 class="chapter-title"><span class="chapter-number">05</span>The Devotional Life</h1>

<section class="column column-left">
  <h2 class="section-heading">I. “This Is Eternal Life”</h2>
  <p><span class="marker">A.</span> Jesus said in John 17:3, “This is eternal life, that they may know You, the only true God, and Jesus Christ whom You have sent.” This “knowledge” is more than a casual acquaintance. Instead, it refers to a deep, meaningful relationship; a personal, experimental [that which is founded on experience] relationship with the Father and the Son.</p>
  <p class="quote">Personal religion among us as a people is at a low ebb. There is much form, much machinery, much tongue religion… What we need is to know God and the power of His love, as revealed in Christ, by an experimental knowledge. – Letters to the Church, vol. 5, p. 743.</p>
  <p><span class="marker">B.</span> Meaningful relationships must be invested in; they must have time and attention to develop. They must have good communication. This communication must be a two-way street. Not only are we to communicate with God, but also receive His communication to us. Not only are we to talk, but we must do some listening, too. The devotional life – talking to God in prayer and listening to God through meditation and the study of His word – is the means of establishing a saving relationship with God. We speak to God in prayer, and He communicates to us through His Word.</p>
  <p class="quote">Enter your closets with the Bible in your hand, and there commune with God, having an ear to hear what the Spirit saith unto you. Let your heart be humbled and teachable, softened and subdued by the Holy Spirit. If you find that your former views are not sustained by the Bible, it is for your eternal interest to learn this as soon as possible; for when God speaks in his word, our preconceived opinions must be yielded up, and our ideas brought into harmony with a “thus saith the Lord.” – Field Notes Quarterly, Dec. 24 1895.</p>
  <p><span class="marker">C.</span> The devil knows this very well, and attempts to do all in his power to derail the devotional exercises of God’s people.</p>
  <p class="quote">An intensity such as never before was seen is taking possession of the world. In amusement, in moneymaking, in the contest for power, in the very struggle for existence, there is a terrible force that engrosses body and mind and soul. In the midst of this maddening rush, God is speaking. He bids us come apart and commune with Him. “Be still, and know that I am God.” Psalm 46:10. Many, even in their seasons of devotion, fail of receiving the blessing of real communion with God. They are in too great haste. With hurried steps they press through the circle of Christ’s loving presence, pausing perhaps a moment within the sacred precincts, but not waiting for counsel. They have no time to remain with the divine Teacher. With their burdens they return to their work. – Foundations, p. 260.</p>
  <p class="quote">Satan well knows that all whom he can lead to neglect prayer and the searching of the Scriptures, will be overcome by his attacks. Therefore he invents every possible device to engross the mind… – The Long Conflict, p. 519.</p>
  <p><span class="marker">D.</span> No amount of prayer or Bible study will help the person who is not willing to apply the truth to his or her practical life. The Bible calls the person who doesn’t practice the truth a self-deceived fool (Ja. 1:22; Mt. 7:26-7). To gain knowledge is only part of the process. Jesus taught that if anyone wanted to know the truth, they must be willing to practice the truth (Jn. 7:17; 12:35). Personal application involves putting into practice the truth that we learn and sharing it with others.</p>
  <p class="quote">Truth is not truth to those who do not practice it. Truth is only truth to you when you live it in the daily life… – Collected Sermons, p. 1744.</p>
  <p class="quote">He who does nothing but pray will soon cease to pray, or his prayers will become a formal routine. When men take themselves out of social life, away from the sphere of Christian duty and cross bearing; when they cease to work earnestly for the Master, who worked earnestly for them, they lose the subject matter of prayer and have no incentive to devotion. – The Narrow Path, p. 101.</p>
</section>

<div class="feature-image" role="img" aria-label="Chapter photograph: a person in quiet prayer with an open Bible"></div>

<section class="column column-right">
  <h2 class="section-heading">II. Personal Prayer <span class="subtitle">– The Key to Spiritual Power</span></h2>
  <p><span class="marker">A.</span> Prayer is the secret to Spiritual power.</p>
  <p><span class="marker">1.</span> Prayer is essential to spiritual life and all spiritual activity. Just as we must have air to breathe in order to stay alive, so we must engage in prayer in order to have spiritual life. Prayer is the breath of the soul. – Workers in the Field, p. 254.</p>
  <p>The darkness of the evil one encloses those who neglect to pray. – Ibid., p. 94.</p>
  <p><span class="marker">2.</span> Without prayer, our religious experience degenerates into a mere outward form, much like the “dry bones” that had the word preached to them, but had not yet received the breath of life (Ezek. 37:7-8). This was the condition of the church in Christ’s day; they searched the Scriptures for information rather than a real relationship with God. Jesus commended their study of the Bible, but added “You are not willing to come to Me that you may have life” (Jn. 5:39-40).</p>
  <p class="quote">[Prayer] is the secret of spiritual power. No other means of grace can be substituted, and the health of the soul be preserved. Prayer brings the heart into immediate contact with the Well-spring of life, and strengthens the sinew and muscle of the religious experience. Neglect the exercise of prayer, or engage in prayer spasmodically, now and then, as seems convenient, and you lose your hold on God. The spiritual faculties lose their vitality, the religious experience lacks health and vigor. – Workers in the Field, p. 254.</p>
  <p><span class="marker">3.</span> This is why we are encouraged to “pray without ceasing” (1 Thes. 5:17). This does not mean to engage in long, drawn-out, formal praying, but to be in an attitude of open communion with God, kind of like being on the phone with someone and not hanging up.</p>
  <p class="quote">Christ commands, “Pray without ceasing;” that is, keep the mind uplifted to God, the source of all power and efficiency.<br>- Counsels to Pastors, p. 510.</p>
  <p class="quote">Unceasing prayer is the unbroken union of the soul with God… - The Narrow Path, p. 97.</p>
  <p class="quote">Pray in your closet, and as you go about your daily labor let your heart be often uplifted to God. It was thus that Enoch walked with God. – Ibid., pp. 98-99.</p>
  <p class="quote">Cultivate the habit of talking with the Saviour when you are alone, when you are walking, and when you are busy with your daily labor. Let the heart be continually uplifted in silent petition for help, for light, for strength, for knowledge. Let every breath be a prayer.<br>– Hours of Prayer, p. 179.</p>
</section>

<div class="folio">Harbor Light Training Manual<span class="page-number">31</span></div>

</body>
</html>
```